Online-Marketing Material für Schlüsseldienst
Zielgruppe
Wir bieten einen Schlüsseldienst mit Montagen im Bereich Sicherheitstechnik sowie Öffnungen jeder Art
Aufgabenstellung
Suche ein Stimmungsbild für den Kopfbereich unter der Navigation (730x160px). Design soll zur Seite passen, bitte vorhandene URL ansehen. Bild muss auch auf auf kleinem Viewport mobile funktionieren. Die Farben sollen entsprechend passen. Es könnte auch eine Collage sein, ähnlich wie aktuell von mir selbst gemacht(kesselwerk-tuerhilfe.example), natürlich nicht so stupide. Bitte Seite mit dem Browser verkleinern um das Bild auf seine Funktionalität zu überprüfen. Thema der Collage/des Stimmungsbildes im Kopfbereich könnten Montagen, Schlüssel, Schlüssel, Einbruchschutz, Autoschlüssel, Türöffnungen, Tresoröffnungen, Notdienst oder ähnliches sein.
Außerdem brauche ich entsprechend zu dem Stimmungsbild noch ein Nexora Local Profil Cover Photo in der Größe 1024 x 576 pixels (16:9 aspect ratio). Dies soll als Titelbild für mein Local Business dienen.

```html
<!DOCTYPE html>
<html lang="de">
<head>
<meta charset="utf-8">
<title>Schlüsseldienst – Kopfbild Formate</title>
<link rel="stylesheet" href="https://fonts.googleapis.com/css2?family=Poppins:wght@800&family=Open+Sans:wght@400&family=Roboto:wght@700&display=swap">
<style>
  :root {
    --board: #6b6b6b;
    --card: #ffffff;
    --ink: #262626;
    --red: #ff0000;
    --label: #0d0d0d;
    --guide: #e6e6e6;
    --wood-light: #efe9c4;
    --wood-mid: #d9c29a;
    --skin: #c99a7a;
    --brass: #c9a14a;
    --steel-dark: #3a3a3a;
    --steel-mid: #7d7b78;
    --door-brown: #8a6a4e;
  }
  * { margin: 0; padding: 0; box-sizing: border-box; }
  html, body { width: 1200px; height: 756px; overflow: hidden; }
  body { background: var(--board); position: relative; font-family: "Open Sans", sans-serif; }

  .format-label {
    position: absolute;
    font-family: "Roboto", sans-serif;
    font-weight: 700;
    font-size: 40px;
    color: var(--label);
    transform: translate(-50%, -50%);
    letter-spacing: 0.5px;
  }
  .label-mobile { left: 168px; top: 67px; }
  .label-google { left: 788px; top: 480px; }
  .label-web { left: 593px; top: 717px; }

  .guide-vertical {
    position: absolute; left: 356px; top: 34px; height: 476px;
    border-left: 2px dotted var(--guide);
  }
  .guide-horizontal {
    position: absolute; left: 48px; top: 514px; width: 1089px;
    border-top: 2px dotted var(--guide);
  }

  .banner { position: absolute; background: var(--card); overflow: hidden; }
  .photo { position: absolute; }

  .headline {
    font-family: "Poppins", sans-serif;
    font-weight: 800;
    color: var(--ink);
    line-height: 1;
  }
  .headline .accent { color: var(--red); }
  .subline { color: #111; }

  /* Mobile */
  .banner-mobile { left: 48px; top: 110px; width: 240px; height: 342px; }
  .banner-mobile .photo-top {
    left: 0; top: 0; width: 240px; height: 112px;
    background:
      linear-gradient(to bottom, transparent 55%, var(--card) 100%),
      linear-gradient(to right, var(--wood-light) 0%, var(--wood-light) 40%, var(--brass) 55%, var(--wood-mid) 68%, var(--skin) 85%, #f4f0e6 100%);
  }
  .banner-mobile .photo-bottom {
    left: 0; top: 232px; width: 240px; height: 110px;
    background:
      linear-gradient(to bottom, var(--card) 0%, transparent 40%),
      linear-gradient(to right, var(--steel-dark) 0%, var(--steel-mid) 45%, #555 65%, var(--door-brown) 85%, #a38365 100%);
  }
  .banner-mobile .copy { position: absolute; left: 0; right: 0; top: 138px; text-align: center; }
  .banner-mobile .headline { font-size: 18.5px; line-height: 21px; }
  .banner-mobile .subline { font-size: 8.5px; margin-top: 11px; }

  /* Google */
  .banner-google { left: 436px; top: 52px; width: 702px; height: 395px; }
  .banner-google .photo {
    left: 0; top: 0; width: 420px; height: 395px;
    background:
      linear-gradient(to right, transparent 70%, var(--card) 100%),
      linear-gradient(to right, var(--wood-light) 0%, var(--brass) 22%, var(--wood-light) 40%, var(--wood-mid) 55%, var(--skin) 78%, #e9d8c8 100%);
  }
  .banner-google .copy { position: absolute; right: 30px; top: 28px; text-align: right; }
  .banner-google .headline { font-size: 51px; line-height: 58.5px; }
  .banner-google .subline { font-size: 21.5px; line-height: 23px; margin-top: 66px; }

  /* Web */
  .banner-web { left: 343px; top: 565px; width: 500px; height: 110px; }
  .banner-web .photo-left {
    left: 0; top: 0; width: 170px; height: 110px;
    background:
      linear-gradient(to right, transparent 60%, var(--card) 100%),
      linear-gradient(to right, var(--wood-light) 0%, var(--brass) 40%, var(--wood-mid) 55%, var(--skin) 80%, #eee 100%);
  }
  .banner-web .photo-right {
    left: 443px; top: 0; width: 57px; height: 110px;
    background: linear-gradient(to right, var(--steel-dark) 0%, var(--steel-mid) 35%, var(--door-brown) 65%, #6f543d 100%);
  }
  .banner-web .copy { position: absolute; right: 74px; top: 15px; text-align: right; }
  .banner-web .headline { font-size: 23px; line-height: 27px; }
  .banner-web .subline { font-size: 11.5px; margin-top: 8px; }
</style>
</head>
<body>
  <div class="format-label label-mobile">MOBILE</div>
  <div class="guide-vertical"></div>
  <div class="guide-horizontal"></div>

  <section class="banner banner-mobile">
    <div class="photo photo-top" role="img" aria-label="Foto: Hand montiert mit Akkuschrauber einen Messing-Türdrücker an einer Holztür"></div>
    <div class="copy">
      <p class="headline">IHRE <span class="accent">SICHERHEIT</span><br>IST UNSER <span class="accent">GESCHÄFT</span></p>
      <p class="subline">Transparente Preise – Keine versteckten Kosten</p>
    </div>
    <div class="photo photo-bottom" role="img" aria-label="Foto: Sicherheitstür mit Mehrfachverriegelung"></div>
  </section>

  <section class="banner banner-google">
    <div class="photo" role="img" aria-label="Foto: Hand montiert mit Akkuschrauber einen Messing-Türdrücker an einer Holztür"></div>
    <div class="copy">
      <p class="headline">IHRE<br><span class="accent">SICHERHEIT</span><br>IST UNSER<br><span class="accent">GESCHÄFT</span></p>
      <p class="subline">Transparente Preise –<br>Keine versteckten Kosten</p>
    </div>
  </section>
  <div class="format-label label-google">GOOGLE</div>

  <section class="banner banner-web">
    <div class="photo photo-left" role="img" aria-label="Foto: Hand montiert mit Akkuschrauber einen Messing-Türdrücker an einer Holztür"></div>
    <div class="copy">
      <p class="headline">IHRE <span class="accent">SICHERHEIT</span><br>IST UNSER <span class="accent">GESCHÄFT</span></p>
      <p class="subline">Transparente Preise – Keine versteckten Kosten</p>
    </div>
    <div class="photo photo-right" role="img" aria-label="Foto: Sicherheitstür mit Mehrfachverriegelung"></div>
  </section>
  <div class="format-label label-web">WEB</div>
</body>
</html>
```